KWT greatest golf app flyer design

I'm an engineer, so without doubt, I need your help. I have a rough draft of two trifold flyers that I need help making look good. I've uploaded the rough drafts and some inspirational images. It should also have room for a QR Code and an Tovel store logo.

Target Market(s)

Golfers

Industry/Entity Type

Engineer

Font styles to use
Serif
Sans Serif

Requirements
Must have
• Appeal. duh
Nice to have
• Open to your ideas. You see the blues, greens, whites and grays used. Keep that color sceme.

```html
<!DOCTYPE html>
<html lang="en">
<head>
<meta charset="utf-8">
<title>KWT Trifold Flyer</title>
<link href="https://fonts.googleapis.com/css2?family=Oswald:wght@400;500;600&family=Source+Sans+3:wght@400;600;700&display=swap" rel="stylesheet">
<style>
:root{
  --blue:#1f7fd1;
  --blue-dark:#155f9e;
  --navy:#1d2b4a;
  --green:#5cb82e;
  --green-light:#9fd84a;
  --green-dark:#2f7d1c;
  --white:#ffffff;
  --paper:#f4f5f6;
  --gray:#e3e6e8;
  --ink:#2b2f33;
  --bg:#d9dcdf;
}
*{box-sizing:border-box;margin:0;padding:0}
html,body{width:1200px;height:1200px;overflow:hidden;background:var(--bg)}
body{position:relative;font-family:"Source Sans 3",Arial,sans-serif;color:var(--ink)}
.spread{position:absolute;left:230px;width:740px;height:574px;background:var(--paper);overflow:hidden;box-shadow:0 4px 14px rgba(0,0,0,.18)}
.spread--outside{top:18px}
.spread--inside{top:608px}
.abs{position:absolute}
.head{font-family:"Oswald",Arial,sans-serif;font-weight:500;color:var(--blue);text-transform:uppercase;line-height:1.05}
.body{font-size:10px;line-height:1.75}

/* outside */
.features{left:0;top:0;width:262px;height:574px;background:linear-gradient(160deg,var(--green-light) 0%,var(--green) 45%,#4aa826 100%)}
.features__photo{position:absolute;left:0;top:0;width:262px;height:140px;background:radial-gradient(circle at 40% 60%,rgba(255,255,255,.75),rgba(255,255,255,0) 60%)}
.features__title{left:16px;top:128px;font-size:19px;color:var(--navy)}
.features__list{left:16px;top:162px;width:240px;list-style:none;font-size:9.6px;font-weight:700;color:var(--navy);line-height:21.3px}
.features__list li{padding-left:14px;position:relative}
.features__list li::before{content:"";position:absolute;left:0;top:8px;width:5px;height:5px;border-radius:50%;background:var(--white)}
.about{left:262px;top:0;width:228px;height:574px;background:var(--white)}
.about__text{left:14px;top:102px;width:186px}
.about__text .head{font-size:19px;margin-bottom:6px}
.about__text p{margin-bottom:6px}
.tagline{font-size:19px;color:var(--green);line-height:1.4}
.tagline--blue{color:var(--blue)}
.contact .head{font-size:13px;margin-top:10px}
.contact p{font-size:10px;font-weight:600}
.wordmark{display:inline-flex;align-items:center;gap:5px;font-family:"Oswald",Arial,sans-serif;font-weight:600;color:var(--blue)}
.wordmark__dot{width:10px;height:10px;border-radius:50%;background:var(--green)}
.cover{left:490px;top:0;width:250px;height:574px;background:linear-gradient(180deg,var(--gray) 0%,var(--white) 40%,var(--green-light) 72%,var(--green-dark) 100%)}
.cover__logo{left:580px;top:28px;font-size:30px}
.cover__photo{left:518px;top:122px;width:204px;height:204px;border-radius:50%;background:linear-gradient(180deg,#9fc8ef 0%,#d8e7f2 40%,#6f8f6a 62%,#3f6d2c 100%)}
.cover__headline{right:18px;top:402px;font-family:"Oswald",Arial,sans-serif;font-weight:600;font-size:44px;line-height:1;text-transform:uppercase}
.cover__headline span{display:block}
.w{color:var(--white)}.n{color:var(--navy)}

/* inside */
.band{left:0;top:0;width:740px;height:574px}
.connect{left:0;top:0;width:262px;height:520px;background:linear-gradient(180deg,#dfeefa 0%,#f4f8f3 60%,rgba(255,255,255,0) 100%)}
.phone{border:4px solid var(--white);border-radius:16px;box-shadow:0 2px 6px rgba(0,0,0,.25)}
.phone--profile{left:14px;top:38px;width:122px;height:222px;background:linear-gradient(180deg,#eef5fb 0%,#cfe4f5 55%,#7ea878 100%)}
.connect__intro{left:148px;top:86px;width:104px}
.connect__intro .head{font-size:24px;margin-bottom:4px}
.connect__intro .lead{color:var(--green)}
.connect__intro p{font-size:10px;line-height:1.55}
.connect__ways{left:16px;top:282px;width:232px;font-size:10px;line-height:1.55}
.hl-blue{font-family:"Oswald",Arial,sans-serif;color:var(--blue);text-transform:uppercase;font-size:12px}
.hl-green{font-family:"Oswald",Arial,sans-serif;color:var(--green);text-transform:uppercase;font-size:12px}
.connect__ways .sub{font-family:"Oswald",Arial,sans-serif;color:var(--blue);font-size:12px;margin-bottom:6px}
.connect__ways .note{font-size:8.5px;margin-top:4px}
.connect__contact{left:16px;top:534px;color:var(--white)}
.connect__contact .head{color:var(--white);font-size:12px}
.connect__contact p{font-size:9.5px}
.panel-title{font-family:"Oswald",Arial,sans-serif;font-weight:500;font-size:22px;color:var(--white);text-transform:uppercase}
.in{left:262px;top:0;width:228px;height:574px}
.in__title{left:14px;top:32px}
.in__text{left:10px;top:104px;width:104px;font-size:9.6px;line-height:1.55}
.in__text .step{display:block;margin-top:2px}
.phone--invite{left:124px;top:92px;width:98px;height:170px;background:linear-gradient(180deg,#f7f8fa,#dfe5ea)}
.in__respond{left:10px;top:290px;width:212px;font-size:9.6px;line-height:1.55}
.phone--setup{left:10px;top:376px;width:104px;height:186px;background:linear-gradient(180deg,#f5f7fa,#d8e3ee)}
.in__setup{left:120px;top:388px;width:104px;font-size:9.6px;line-height:1.55}
.play{left:490px;top:0;width:250px;height:574px}
.play__title{left:14px;top:32px}
.play__text{left:14px;top:134px;width:112px;font-size:9.6px;line-height:1.55}
.play__text .step{display:block;margin-top:4px}
.phone--group{left:130px;top:64px;width:112px;height:194px;background:linear-gradient(180deg,#f7f9fb,#dce6ef)}
.phone--card{left:134px;top:272px;width:108px;height:186px;background:linear-gradient(180deg,#eef4fb,#cfdfee)}
.play__end{left:14px;top:494px;width:230px;font-size:9.4px;line-height:1.45;color:var(--navy)}
</style>
</head>
<body>

<section class="spread spread--outside">
  <div class="abs features">
    <div class="features__photo" role="img" aria-label="Close-up photo of a golf ball in the grass"></div>
    <h2 class="abs head features__title">A Few KWT Features</h2>
    <ul class="abs features__list">
      <li>Automated invite and field management</li>
      <li>Over 1M gaming combinations</li>
      <li>Instant add of guests at the 1st tee</li>
      <li>Easy add of paper scorecards</li>
      <li>Community-wide game definitions</li>
      <li>Handicap Tracked Games (no sandbagging)</li>
      <li>Find a Game feature</li>
      <li>Nationwide course database</li>
      <li>Tovel phone contacts accessible</li>
      <li>Custom Nassau management – any nassau with a particular golf buddy has the custom settings you both want</li>
      <li>Personal stat reporting</li>
      <li>Personal game preferences</li>
      <li>Real-time Leaderboard and Standings</li>
      <li>Texting of Final Results</li>
      <li>Handles fivesomes and plus handicaps</li>
      <li>Many more…</li>
    </ul>
  </div>

  <div class="abs about">
    <div class="abs about__text body">
      <h2 class="head">Kingswood Tee</h2>
      <p>The only comprehensive Golf Networking and multi group Gaming platform you'll find.</p>
      <p>Built by golfers for golfers. Every screen, every feature has come from the field up. KWT is the only golf app that's been specifically designed and built for the GOLFER. Not for the advertising, not for annoying pop-ups or ads, not for constant and useless feeds.</p>
      <p>We built KWT for the golfer to get more fun out of the game they love. Easily find, connect and grow a great circle of golf buddies.</p>
      <div class="head tagline tagline--blue">Get in a bigger game</div>
      <div class="head tagline">Get Kingswood Tee</div>
      <div class="contact">
        <div class="head">Contact Us</div>
        <p>kwtcustserv@kingswoodtee.net</p>
      </div>
      <div class="wordmark" style="font-size:20px;margin-top:14px"><span class="wordmark__dot"></span>KWT</div>
    </div>
  </div>

  <div class="abs cover"></div>

  <svg class="abs" style="left:0;top:0" width="740" height="574" viewBox="0 0 740 574" aria-hidden="true">
    <path d="M395 0 C450 40 472 110 474 200 L478 574 L486 574 L482 200 C480 100 458 35 412 0Z" fill="var(--blue)"/>
    <path d="M425 0 C478 35 494 105 494 190 L492 574 L498 574 L500 190 C500 95 486 30 440 0Z" fill="var(--green)"/>
    <circle cx="620" cy="224" r="108" fill="none" stroke="var(--green)" stroke-width="6"/>
    <path d="M512 224 A108 108 0 0 1 620 116" fill="none" stroke="var(--blue)" stroke-width="7"/>
  </svg>

  <div class="abs wordmark cover__logo"><span class="wordmark__dot"></span>KWT</div>
  <div class="abs cover__photo" role="img" aria-label="Photo of a winding golf cart path along a seaside course at sunset"></div>
  <h1 class="abs cover__headline"><span class="w">Connect</span><span class="n">You're In</span><span class="w">Let's Play!</span></h1>
</section>

<section class="spread spread--inside">
  <svg class="abs band" viewBox="0 0 740 574" aria-hidden="true">
    <path d="M0 0 H740 V40 C600 60 520 90 490 120 C420 70 340 60 262 80 V0Z" fill="var(--blue)"/>
    <path d="M262 80 C340 60 420 70 490 120" fill="none" stroke="var(--green)" stroke-width="4"/>
    <path d="M490 120 C520 90 600 60 740 40" fill="none" stroke="var(--green)" stroke-width="4"/>
    <path d="M0 515 C200 490 400 470 740 480 V574 H0Z" fill="var(--green)"/>
    <path d="M0 540 C250 520 480 505 740 510 V574 H0Z" fill="var(--green-dark)"/>
  </svg>
  <div class="abs connect"></div>

  <div class="abs phone phone--profile" role="img" aria-label="App screen showing the home menu with network, games and profile buttons"></div>
  <div class="abs connect__intro">
    <h2 class="head">Connect</h2>
    <p><span class="lead">Connect to other golfers</span> who share your same passion for the game.</p>
    <p style="margin-top:8px">KWT "Communities" are your view to other golfers.</p>
  </div>
  <div class="abs connect__ways">
    <div class="sub">Join a Community in any of the following ways:</div>
    <div><span class="hl-green">1. Use a promo code</span> when registering.*</div>
    <div><span class="hl-green">2. Search communities</span> by zip code and request to join.</div>
    <div><span class="hl-green">3. Be found</span> Community Managers search for members and send invites.</div>
    <div><span class="hl-green">4. Create and manage your own</span> Community.</div>
    <div class="sub" style="margin-top:10px">Join 1, 2, 3… as many communities as you see fit.</div>
    <div class="note">* Contact KWT if you'd like help with registering groups.</div>
  </div>
  <div class="abs connect__contact">
    <div class="head">Contact Us</div>
    <p>kwtcustserv@kingswoodtee.net</p>
  </div>

  <div class="abs in">
    <div class="abs panel-title in__title">You're In</div>
    <div class="abs in__text">
      <div class="hl-green" style="font-size:11px">Get in a game!</div>
      A few ways in KWT to do that:
      <span class="step"><span class="hl-blue">1. Search for a game.</span> You can see upcoming games and descriptions setup by people in your Communities. From the KWT app, send a request to join the game.</span>
    </div>
    <div class="abs phone phone--invite" role="img" aria-label="Text message inviting a player to join a game"></div>
    <div class="abs in__respond"><span class="hl-blue">2. Respond to game invites</span><br>When a game is setup, invite texts are sent to the members in the game admins game roster. Reply yes, and KWT automatically puts you into the Field</div>
    <div class="abs phone phone--setup" role="img" aria-label="App screen for game setup details"></div>
    <div class="abs in__setup"><span class="hl-blue">3. Setup your own game</span> and invite players from your communities or your phone contacts.</div>
  </div>

  <div class="abs play">
    <div class="abs panel-title play__title">Let's Play!</div>
    <div class="abs play__text">
      <div class="hl-green" style="font-size:11px">Game Day!</div>
      Show up, login to the KWT app and we'll take you to your scorecard for the game.
      <span class="step"><span class="hl-blue">1. Select the players in your group</span> from the field. Easily add any Guests or Players who happen to show up or who haven't registered yet.</span>
      <span class="step"><span class="hl-blue">2. Use the KWT scorecard</span> for recording scores</span>
      <span class="step"><span class="hl-blue">3. View real-time leaderboards</span> and Standings</span>
    </div>
    <div class="abs phone phone--group" role="img" aria-label="App screen for choosing players in a group"></div>
    <div class="abs phone phone--card" role="img" aria-label="App scorecard screen with hole scores"></div>
    <div class="abs play__end">At the end of the Round, the Game Manager can edit scores, settings, even add a paper scorecard to the game.<br>When Results are posted as Final, texts results can be sent to players wanting them.</div>
  </div>
</section>

</body>
</html>
```